New Business card

Wanting to update my current business card to reflect our major marketing differentiation: We hire artists, and teach them the art of painting.

Currently I use a Fotelux frame for my profile pic, but want it to look like it is a hand drawn or painting on a canvas.

I want the look at feel of the card to be consistent with our website, as well as other print materials.
The back of the card should not have much written on it (i like the space for making notes), but is a good place for a few key pieces of information.

Needs to include
Paul Dorsey
www.corvelhome.com
paul@corvelhome.com
555-018-2273
Crafted by Hand...Finished with Care. (tm)

If other images (such as the ones on my current card) are needed, please ask, but I did not think we needed them.

I am not sure why all the submissions coming in have no pictures on them, but I thought I was clear that I wanted my picture on the card, but in a creative and artistic way. My idea was that it would look like someone painted it (I thought there was software that did this). I do not like any of the cards that have no pictures on them.

```html
<!DOCTYPE html>
<html lang="en">
<head>
<meta charset="utf-8">
<title>Corvel Home – Business Card</title>
<link rel="stylesheet" href="https://fonts.googleapis.com/css2?family=Cinzel:wght@600&family=Open+Sans:wght@400;600&display=swap">
<style>
  :root {
    --page: #e8e5e0;
    --white: #ffffff;
    --ink: #141414;
    --black: #0e0e0e;
    --charcoal: #222222;
    --gold: #c99a3a;
    --gold-light: #f1d58a;
    --gold-deep: #9c7224;
    --text-light: #f2f2f2;
    --mist: #ece9e4;
  }
  * { box-sizing: border-box; margin: 0; padding: 0; }
  html, body { width: 1200px; height: 784px; overflow: hidden; }
  body {
    background: var(--page);
    font-family: "Open Sans", Arial, sans-serif;
    position: relative;
  }
  .card {
    position: absolute;
    top: 237px;
    width: 540px;
    height: 309px;
    overflow: hidden;
    box-shadow: 0 6px 18px rgba(0,0,0,0.18);
  }
  .card--back { left: 40px; background: var(--white); }
  .card--front { left: 620px; background: var(--white); }

  /* back */
  .back__interior {
    position: absolute; inset: 0;
    background: linear-gradient(160deg, #f6f4f1 0%, var(--mist) 45%, #dcd6cd 100%);
  }
  .back__logo {
    position: absolute; right: 34px; bottom: 58px;
    font-family: "Cinzel", Georgia, serif; font-weight: 600;
    font-size: 15px; letter-spacing: 4px; color: var(--ink);
  }

  /* front */
  .front__header {
    position: absolute; left: 0; top: 0; width: 100%; height: 150px;
    background: var(--white); text-align: center;
  }
  .front__logo {
    position: absolute; left: 0; right: 0; top: 46px;
    font-family: "Cinzel", Georgia, serif; font-weight: 600;
    font-size: 32px; letter-spacing: 9px; color: var(--ink);
  }
  .front__tagline {
    position: absolute; left: 0; right: 0; top: 104px;
    font-family: "Cinzel", Georgia, serif; font-weight: 600;
    font-size: 15px; letter-spacing: 2px; color: var(--gold);
  }
  .front__band {
    position: absolute; left: 0; top: 150px; width: 100%; height: 8px;
    background: linear-gradient(90deg, var(--gold-deep), var(--gold-light) 50%, var(--gold-deep));
  }
  .front__panel {
    position: absolute; left: 0; top: 158px; width: 100%; height: 151px;
    background: linear-gradient(180deg, var(--charcoal), var(--black));
  }
  .front__portrait {
    position: absolute; left: 0; top: 0; width: 230px; height: 151px;
    background: linear-gradient(90deg, #d9a43e 0%, #a87a2a 22%, #3a3026 42%, #1c1c1c 100%);
  }
  .front__contact {
    position: absolute; left: 300px; top: 18px; color: var(--text-light);
  }
  .contact__name {
    font-weight: 600; font-size: 17px; color: var(--gold); margin-bottom: 10px;
  }
  .contact__line {
    display: flex; align-items: center; gap: 8px;
    font-size: 13.5px; line-height: 22px; letter-spacing: 0.3px;
  }
  .contact__icon { width: 13px; height: 13px; flex: none; }
</style>
</head>
<body>

<section class="card card--back" aria-label="Card back">
  <div class="back__interior" role="img" aria-label="Faded photo of a bright living room interior with a stone fireplace"></div>
  <div class="back__logo">CORVEL HOME</div>
</section>

<section class="card card--front" aria-label="Card front">
  <header class="front__header">
    <div class="front__logo">CORVEL HOME</div>
    <div class="front__tagline">Crafted by Hand...Finished with Care</div>
  </header>
  <div class="front__band"></div>
  <div class="front__panel">
    <div class="front__portrait" role="img" aria-label="Painted-style portrait of the owner holding a brush beside a textured gold wall"></div>
    <div class="front__contact">
      <div class="contact__name">Paul Dorsey</div>
      <div class="contact__line">
        <svg class="contact__icon" viewBox="0 0 14 14" aria-hidden="true">
          <g fill="none" stroke="#c99a3a" stroke-width="1.2">
            <circle cx="7" cy="7" r="6"/><ellipse cx="7" cy="7" rx="2.6" ry="6"/>
            <line x1="1" y1="7" x2="13" y2="7"/>
          </g>
        </svg>
        <span>www.corvelhome.com</span>
      </div>
      <div class="contact__line">
        <svg class="contact__icon" viewBox="0 0 14 14" aria-hidden="true">
          <rect x="1" y="3" width="12" height="8.5" fill="#c99a3a"/>
          <polyline points="1,3 7,8 13,3" fill="none" stroke="#0e0e0e" stroke-width="1.1"/>
        </svg>
        <span>paul@corvelhome.com</span>
      </div>
      <div class="contact__line">
        <svg class="contact__icon" viewBox="0 0 14 14" aria-hidden="true">
          <path d="M3 1.5 L5.2 1.5 L6 4.3 L4.6 5.5 Q5.8 8.2 8.5 9.4 L9.7 8 L12.5 8.8 L12.5 11 Q12.5 12.5 11 12.5 Q1.5 11.8 1.5 3 Q1.5 1.5 3 1.5 Z" fill="#c99a3a"/>
        </svg>
        <span>555-018-2273</span>
      </div>
    </div>
  </div>
</section>

</body>
</html>
```